Publisher needs a book cover design for ‘Lanterns Over the Marsh Gate’ book

We need a book cover (front, back, spine) for the 2nd edition of a book entitled ‘Lanterns Over the Marsh Gate’ and subtitled ‘the quiet geography of tidal winds, ferry routes and harbour lanterns’ (inverted commas not to be part of the title and subtitle). The author is Rupert Calloway. The publisher is Vellmark Press. The finished size of the paperback version will be the industry standard 9" x 6". There will be paperback, hardback, and e-book versions. The final number of pages is expected to be in the region 150-180 pages. Text for the back cover is not yet available, but at the bottom of the back cover should be publisher logo (rectangular) on the left and space for the ISBN bar code on the right. The circular logo should be on the spine. The design should be original and not include any stock images that have been created by someone else or may require obtaining a copyright licence to use. Symbols in common use and not copyrighted are probably ok. There are no required images, photographs or symbols except the publisher logo at the left bottom of the back cover and lower spine. Spine lettering should be UK/US style with the top of the writing nearest the front cover. The designer is free to be creative using appropriate diagrams, symbols or abstract designs. Rectangular and circular variants of the publisher logo are attached. Designers are assured that when evaluating designs absolutely no notice whatsoever is taken of a designer's Pixo Rally ranking or status; We are completely output driven, so what matters is the design, not the ranking or status of the designer. In a similar way, designs are not evaluated as 'good' or 'bad' - the winning design will be chosen after review by a design review panel and is not decided arbitrarily by a single person. All submitted designs should be capable of effective copyright assignment.

Target Market(s)

Practitioners, parents, teachers, pupils and academics concerned with child protection, safeguarding and the elimination of emotional abuse of children in the classroom

Font styles to use
Serif
Sans Serif

Requirements
Must have
• • Title, author, edition, subtitle, publisher logo
Nice to have
• • Originality, innovation
Should not have
• • Stock images or anything else requiring additional copyright discussions and negotiations.

```html
<!DOCTYPE html>
<html lang="en">
<head>
<meta charset="utf-8">
<title>Lanterns Over the Marsh Gate — Cover Spread</title>
<link rel="stylesheet" href="https://fonts.googleapis.com/css2?family=Lora:ital,wght@0,400;0,700;1,400&display=swap">
<style>
  :root {
    --accent: #e4572e;
    --badge: #e8673f;
    --ink: #2b2b2b;
    --paper: #ffffff;
    --stage: #ffffff;
    --photo-a: #c9d3dc;
    --photo-b: #8fa3b5;
  }
  * { margin: 0; padding: 0; box-sizing: border-box; }
  html, body { width: 745px; height: 1200px; overflow: hidden; background: var(--stage); }
  .canvas { position: relative; width: 745px; height: 1200px; }
  .spread {
    position: absolute; left: 0; top: 328px; width: 745px; height: 544px;
    background: var(--paper); font-family: 'Lora', Georgia, serif; color: var(--ink);
  }
  .title-bar { position: absolute; width: 2px; background: var(--accent); }
  .title { position: absolute; color: var(--accent); font-weight: 400; }
  .title .strong { font-weight: 700; display: block; }
  .title .line { display: block; }

  /* back cover */
  .back { position: absolute; left: 0; top: 0; width: 348px; height: 544px; }
  .back .title-bar { left: 45px; top: 30px; height: 72px; }
  .back .title { left: 53px; top: 26px; font-size: 24px; line-height: 26px; }
  .blurb { position: absolute; left: 52px; top: 114px; width: 256px; font-size: 9.6px; line-height: 15px; font-style: italic; text-align: justify; hyphens: auto; }
  .blurb p + p { margin-top: 15px; }
  .imprint { position: absolute; left: 52px; top: 484px; display: flex; align-items: center; gap: 5px; font-size: 11px; color: var(--ink); letter-spacing: 0.5px; }
  .imprint .mark { width: 16px; height: 16px; border-radius: 50%; background: var(--ink); }

  /* spine */
  .spine { position: absolute; left: 348px; top: 0; width: 38px; height: 544px; }
  .spine-edition, .spine-title { position: absolute; left: 50%; transform: translateX(-50%); writing-mode: vertical-rl; white-space: nowrap; }
  .spine-edition { top: 30px; font-size: 12px; color: var(--ink); }
  .spine-title { top: 138px; font-size: 16px; color: var(--accent); }
  .spine-title b { font-weight: 700; }
  .spine-mark { position: absolute; left: 13px; top: 497px; width: 12px; height: 12px; border-radius: 50%; background: var(--ink); }

  /* front cover */
  .front { position: absolute; left: 386px; top: 0; width: 359px; height: 544px; }
  .cover-photo {
    position: absolute; left: 0; top: 0; width: 359px; height: 262px;
    background: linear-gradient(180deg, var(--photo-a) 0%, var(--photo-b) 45%, rgba(201,211,220,0.5) 78%, var(--paper) 100%);
  }
  .edition-badge {
    position: absolute; left: 255px; top: 210px; width: 80px; height: 80px; border-radius: 50%;
    background: var(--badge); color: #fff; text-align: center; padding-top: 15px;
  }
  .edition-badge .num { display: block; font-size: 24px; line-height: 24px; }
  .edition-badge .word { display: block; font-size: 14px; line-height: 16px; }
  .front .title-bar { left: 31px; top: 284px; height: 130px; }
  .front .title { left: 46px; top: 283px; font-size: 38px; line-height: 44px; }
  .subtitle { position: absolute; left: 46px; top: 430px; width: 300px; font-size: 13.5px; line-height: 19px; font-style: italic; }
  .author { position: absolute; left: 46px; top: 490px; font-size: 20px; }
</style>
</head>
<body>
<div class="canvas">
  <div class="spread">
    <section class="back">
      <div class="title-bar"></div>
      <h2 class="title"><span class="line">Lanterns</span><span class="line">Over the Marsh</span><span class="strong">Gate</span></h2>
      <div class="blurb">
        <p>Lorem ipsum dolor sit amet, nam id singulis pertinax inciderint. Cum liber omnes scriptorem ei, mei ne dicit partiendo. Sea detracto definitionem cu, tempor vidisse iuvaret his no. Ei affert urbanitas pro, sed no eros semper, fierent omittam philosophia has cu.</p>
        <p>Vix probo malorum deleniti an. Soleat menandri vulputate pri an, eu duo consul tincidunt. Nam in iusto mollis maiorum, mazim maiorum id eam. Sit solet minimum nominavi ad. Vel dicunt delectus molestiae ad. Probo sapientem definitionem sea in.</p>
        <p>In mucius elaboraret delicatissimi sed. Ei aeque aliquando adversarium pri, ei quas invidunt explicari sed. Has sale blandit cu, cu dicta sonet insolens mei. Cu dolorum corrumpit duo. Nam prompta scripserit voluptatibus et.</p>
        <p>Augue definitionem in usu. Ne vel timeam vituperata, eu has audire reprimique. No nec inani regione, nec cu malis vivendo, ne scripta expetenda eos. In salutandi qualisque sed. Pro partem percipit maluisset in, eu eum eleifend mnesarchum.</p>
      </div>
      <div class="imprint"><span class="mark"></span><span>VELLMARK PRESS</span></div>
    </section>

    <section class="spine">
      <div class="spine-edition">2nd Edition</div>
      <div class="spine-title">Lanterns Over the Marsh <b>Gate</b></div>
      <div class="spine-mark" aria-label="Vellmark Press"></div>
    </section>

    <section class="front">
      <div class="cover-photo" role="img" aria-label="Cover photograph area: harbour scene fading into the white page"></div>
      <div class="edition-badge"><span class="num">2nd</span><span class="word">edition</span></div>
      <div class="title-bar"></div>
      <h1 class="title"><span class="line">Lanterns</span><span class="line">Over the Marsh</span><span class="strong">Gate</span></h1>
      <p class="subtitle">the quiet geography of tidal winds, ferry routes and harbour lanterns</p>
      <p class="author">Rupert Calloway</p>
    </section>
  </div>
</div>
</body>
</html>
```